Warranty Card Design for Mattress Brand

We would like to design a warranty card for our mattresses,
it consists of 2 pages in one card (front and back) to be neatly showing our warranty details/text , our logo , our website, address and telephone clearly.

Target Market(s)

household

Font styles to use
Serif
Script

Colors
3277b5
33a6d7
85cae6
0492cd
3176b5
0355a3
85abd2
cee9f5
85acd3

Requirements
Must have
• a nice warranty logo
Nice to have
• a nice warranty logo with a neat text and clear layout, colors have to be related to the logo

```html
<!DOCTYPE html>
<html lang="en">
<head>
<meta charset="utf-8">
<title>Warranty Card</title>
<link href="https://fonts.googleapis.com/css2?family=Quicksand:wght@400;500;600;700&display=swap" rel="stylesheet">
<style>
  :root {
    --brand-blue: #4f79bd;
    --ink: #2e2e33;
    --ink-soft: #3a3a40;
    --faint: #dcdcdc;
    --footer-bg: #f1f1f3;
    --icon-bg: #e6e7ea;
    --page: #ffffff;
    --edge: #d6d6d6;
  }
  * { margin: 0; padding: 0; box-sizing: border-box; }
  html, body { width: 1200px; height: 849px; overflow: hidden; background: var(--page); }
  body { font-family: "Quicksand", sans-serif; color: var(--ink); }

  .card {
    position: relative;
    width: 1200px;
    height: 849px;
    background: var(--page);
    border: 1px solid var(--edge);
    overflow: hidden;
  }

  .title-box {
    position: absolute;
    left: 70px; top: 101px;
    width: 175px; height: 49px;
    border: 2px solid var(--brand-blue);
    color: var(--brand-blue);
    font-weight: 700;
    font-size: 25px;
    display: flex; align-items: center; justify-content: center;
  }

  .brand-name {
    position: absolute;
    right: 60px; top: 78px;
    display: flex; align-items: center; gap: 14px;
    color: var(--brand-blue);
    font-weight: 500;
    font-size: 62px;
    letter-spacing: 1px;
  }
  .brand-name .dot {
    width: 18px; height: 18px; border-radius: 50%;
    background: var(--brand-blue);
  }

  .brand-faint {
    position: absolute;
    left: 250px; top: 420px;
    font-size: 190px;
    font-weight: 500;
    color: var(--faint);
    opacity: 0.7;
    letter-spacing: 4px;
    line-height: 1;
    z-index: 0;
    white-space: nowrap;
  }

  .terms {
    position: absolute;
    left: 66px; top: 256px;
    width: 1080px;
    z-index: 1;
    font-size: 16.6px;
    line-height: 21.8px;
  }
  .terms h2 {
    font-size: 16.6px;
    font-weight: 700;
    color: var(--ink);
    margin-bottom: 9px;
  }
  .terms ul { list-style: none; margin-bottom: 19px; }
  .terms li {
    position: relative;
    padding-left: 27px;
    color: var(--ink-soft);
    font-weight: 500;
  }
  .terms li::before {
    content: "";
    position: absolute;
    left: 11px; top: 8px;
    width: 6px; height: 6px;
    background: var(--ink);
    transform: rotate(45deg);
  }

  .footer-band {
    position: absolute;
    left: 0; top: 699px;
    width: 100%; height: 14px;
    background: var(--brand-blue);
  }
  .footer {
    position: absolute;
    left: 0; top: 713px;
    width: 100%; height: 136px;
    background: linear-gradient(120deg, #f6f6f7 0%, var(--footer-bg) 60%, #ececef 100%);
  }
  .company {
    position: absolute;
    right: 20px; top: 28px;
    text-align: right;
  }
  .company-name { font-weight: 700; font-size: 19px; color: var(--ink); }
  .company-address { font-weight: 500; font-size: 19px; color: var(--ink-soft); margin-top: 6px; }

  .contacts {
    position: absolute;
    right: 20px; top: 90px;
    display: flex; align-items: center; gap: 36px;
    font-size: 14.5px; font-weight: 500; color: var(--ink-soft);
  }
  .contact { display: flex; align-items: center; gap: 14px; }
  .icon {
    width: 44px; height: 44px; border-radius: 50%;
    background: var(--icon-bg);
    display: flex; align-items: center; justify-content: center;
  }
  .icon svg { width: 22px; height: 22px; fill: var(--brand-blue); }
</style>
</head>
<body>
<main class="card">
  <div class="title-box">Warranty</div>

  <div class="brand-name"><span class="dot"></span>Duskrest</div>

  <div class="brand-faint" aria-hidden="true">Duskrest</div>

  <section class="terms">
    <h2>This limited Mattress Warranty applies to the following Defects:</h2>
    <ul>
      <li>Coils or wires that are broken or piercing through fabric.</li>
      <li>Sagging, that measures 3cm or greater (being properly measured) only if the mattress has been continuously supported by appropriate and solid foundation</li>
    </ul>
    <h2>This limited Mattress Warranty does not cover the following:</h2>
    <ul>
      <li>Comfort preference</li>
      <li>Fabric Stains, soiling or burns</li>
      <li>Body impressions of less than 3cm</li>
      <li>Damage to the mattress due to abuse</li>
      <li>Bent Perimeter border rods due to moving or bending the mattress</li>
      <li>Size allowance of +/- 2cm</li>
      <li>Bed Bugs and Dust Mites</li>
      <li>Mattress Odor: as in any upholstery, new mattress may have odor that will fade with time</li>
      <li>For Latex and Memory Foam mattresses: normal change in softness and recovery time in these materials with time. This does not affect the relieving qualities of these mattresses.</li>
      <li>Transportation and Inspection Costs</li>
    </ul>
  </section>

  <div class="footer-band"></div>
  <footer class="footer">
    <div class="company">
      <div class="company-name">Hadi Saleh and Sons</div>
      <div class="company-address">Cedar Hill, Factory Road, Keserwan, Lebanon</div>
    </div>
    <div class="contacts">
      <div class="contact">
        <span class="icon">
          <svg viewBox="0 0 24 24" aria-hidden="true"><path d="M6.6 10.8a15.1 15.1 0 0 0 6.6 6.6l2.2-2.2c.3-.3.7-.4 1-.2 1.1.4 2.3.6 3.6.6.6 0 1 .4 1 1V20c0 .6-.4 1-1 1A17 17 0 0 1 3 4c0-.6.4-1 1-1h3.5c.6 0 1 .4 1 1 0 1.3.2 2.5.6 3.6.1.3 0 .7-.2 1z"/></svg>
        </span>
        <span>+961 1 555 014</span>
      </div>
      <div class="contact">
        <span class="icon">
          <svg viewBox="0 0 24 24" aria-hidden="true"><path d="M12 2a10 10 0 1 0 0 20 10 10 0 0 0 0-20zm0 2c1 0 2.3 1.9 2.8 5H9.2C9.7 5.9 11 4 12 4zM9 11h6a17 17 0 0 1 0 2H9a17 17 0 0 1 0-2zm-2 0a19 19 0 0 0 0 2H4.1a8 8 0 0 1 0-2zm10 0h2.9a8 8 0 0 1 0 2H17a19 19 0 0 0 0-2zm-7.8 4h5.6c-.5 3.1-1.8 5-2.8 5s-2.3-1.9-2.8-5z"/></svg>
        </span>
        <span>www.hadisalehandsons.com</span>
      </div>
    </div>
  </footer>
</main>
</body>
</html>
```